Automotive component supplier needs a business card design

We need a business card design for our company called Velmar Global Components Ltd based in the UK. We are a supplier of interior and exterior components to premium car manufacturers such as Corvane Hale, Durrant Fyfe, Maxtorn and Valdessimo. We would like to see a modern business card design that uses the colour blue.

Target Market(s)

Premium automotive car manufacturers.

Industry/Entity Type

Automotive

Contact Information for Business Card

Company Name : Velmar Global Components Limited
Address: 17 Tamsey Yard, Upper Drisk, Kelbridge, KX31 8RJ, United Kingdom
Web Address : www.velmarparts-example.co.uk

Font styles to use
Other font styles liked:
• Helvetica

Colors
3176b5
0255a3
85acd3
cfdeed
cee9f5
85cae6
34a6d7
0692cd
9bcb3c

Requirements
Must have
• Clear company logo and a mixture of blue colours.
Nice to have
• A high quality modern image.
Should not have
• Multiple colours.

```html
<!DOCTYPE html>
<html lang="en">
<head>
<meta charset="utf-8">
<title>Velmar Global Components – Business Card</title>
<link href="https://fonts.googleapis.com/css2?family=Questrial&display=swap" rel="stylesheet">
<style>
  :root {
    --bg: #e9ebee;
    --card: #ffffff;
    --brand: #0692cd;
    --sky: #29abe2;
    --azure: #1b75bc;
    --navy: #1f2731;
    --ink: #1f2731;
  }
  * { margin: 0; padding: 0; box-sizing: border-box; }
  html, body {
    width: 1200px; height: 801px; overflow: hidden;
    background: var(--bg);
    font-family: "Questrial", Helvetica, Arial, sans-serif;
    color: var(--ink);
  }
  .card {
    position: absolute; top: 273px;
    width: 480px; height: 267px;
    background: var(--card);
    overflow: hidden;
    box-shadow: 0 2px 6px rgba(0,0,0,.18);
  }
  .card--front { left: 110px; }
  .card--back { left: 635px; }
  .card__swoosh { position: absolute; inset: 0; width: 100%; height: 100%; }

  .wordmark { position: absolute; color: var(--brand); font-weight: 400; line-height: 1; white-space: nowrap; }
  .wordmark__name { display: block; }
  .wordmark__tagline { display: block; }
  .card--front .wordmark { left: 78px; top: 84px; }
  .card--front .wordmark__name { font-size: 76px; letter-spacing: 6px; }
  .card--front .wordmark__tagline { font-size: 18px; letter-spacing: 6.5px; margin-top: 4px; }
  .card--back .wordmark { left: 40px; top: 39px; }
  .card--back .wordmark__name { font-size: 44px; letter-spacing: 2px; }
  .card--back .wordmark__tagline { font-size: 10px; letter-spacing: 4px; margin-top: 1px; }

  .contact { position: absolute; left: 267px; top: 50px; list-style: none; }
  .contact__row { display: flex; align-items: flex-start; margin-bottom: 7px; }
  .contact__icon {
    width: 31px; height: 31px; border-radius: 50%;
    flex: none; display: flex; align-items: center; justify-content: center;
    margin-right: 14px;
  }
  .contact__icon--phone { background: var(--sky); }
  .contact__icon--web { background: var(--azure); }
  .contact__icon--pin { background: var(--navy); }
  .contact__text { font-size: 12.5px; line-height: 14.5px; padding-top: 1px; white-space: nowrap; }
  .contact__text--small { font-size: 11px; }
  .contact__row--ruled .contact__text::after {
    content: ""; display: block; width: 64px; height: 2px;
    background: var(--sky); margin-top: 3px;
  }
</style>
</head>
<body>

<section class="card card--front" aria-label="Business card front">
  <svg class="card__swoosh" viewBox="0 0 600 334" preserveAspectRatio="none" aria-hidden="true">
    <path d="M300 0 Q470 60 600 178 L600 0 Z" fill="var(--sky)"/>
    <path d="M340 0 Q490 55 600 150 L600 0 Z" fill="var(--azure)"/>
    <path d="M400 0 Q520 45 600 120 L600 0 Z" fill="var(--sky)"/>
    <path d="M440 0 Q540 35 600 95 L600 0 Z" fill="var(--azure)"/>
    <path d="M480 0 Q560 25 600 70 L600 0 Z" fill="var(--navy)"/>
    <path d="M0 245 Q170 255 312 334 L0 334 Z" fill="var(--navy)"/>
    <path d="M0 158 Q120 262 250 334 L0 334 Z" fill="var(--sky)"/>
    <path d="M0 200 Q110 285 210 334 L0 334 Z" fill="var(--azure)"/>
    <path d="M0 248 Q80 300 140 334 L0 334 Z" fill="var(--navy)"/>
  </svg>
  <div class="wordmark">
    <span class="wordmark__name">VELMAR</span>
    <span class="wordmark__tagline">GLOBAL COMPONENTS</span>
  </div>
</section>

<section class="card card--back" aria-label="Business card back">
  <svg class="card__swoosh" viewBox="0 0 600 334" preserveAspectRatio="none" aria-hidden="true">
    <path d="M0 240 Q170 255 315 334 L0 334 Z" fill="var(--navy)"/>
    <path d="M0 155 Q120 262 250 334 L0 334 Z" fill="var(--sky)"/>
    <path d="M0 198 Q110 285 210 334 L0 334 Z" fill="var(--azure)"/>
    <path d="M0 246 Q80 300 140 334 L0 334 Z" fill="var(--navy)"/>
  </svg>
  <div class="wordmark">
    <span class="wordmark__name">VELMAR</span>
    <span class="wordmark__tagline">GLOBAL COMPONENTS</span>
  </div>
  <ul class="contact">
    <li class="contact__row contact__row--ruled">
      <span class="contact__icon contact__icon--phone">
        <svg width="13" height="13" viewBox="0 0 24 24" aria-hidden="true"><path fill="#fff" d="M6.6 10.8a15 15 0 0 0 6.6 6.6l2.2-2.2c.3-.3.7-.4 1-.2 1.1.4 2.3.6 3.6.6.6 0 1 .4 1 1V20c0 .6-.4 1-1 1A17 17 0 0 1 3 4c0-.6.4-1 1-1h3.5c.6 0 1 .4 1 1 0 1.3.2 2.5.6 3.6.1.3 0 .7-.2 1z"/></svg>
      </span>
      <span class="contact__text">01632 960 014<br>01632 960 015</span>
    </li>
    <li class="contact__row contact__row--ruled">
      <span class="contact__icon contact__icon--web">
        <svg width="13" height="13" viewBox="0 0 24 24" aria-hidden="true"><circle cx="12" cy="12" r="9" fill="none" stroke="#fff" stroke-width="2"/><path d="M3 12h18M12 3c3 3 3 15 0 18M12 3c-3 3-3 15 0 18" fill="none" stroke="#fff" stroke-width="1.6"/></svg>
      </span>
      <span class="contact__text contact__text--small">hello@velmar-example.co.uk<br>www.velmarparts-example.co.uk</span>
    </li>
    <li class="contact__row">
      <span class="contact__icon contact__icon--pin">
        <svg width="12" height="14" viewBox="0 0 24 28" aria-hidden="true"><path fill="#fff" d="M12 0a9 9 0 0 0-9 9c0 7 9 19 9 19s9-12 9-19a9 9 0 0 0-9-9zm0 12.5A3.5 3.5 0 1 1 12 5.5a3.5 3.5 0 0 1 0 7z"/></svg>
      </span>
      <span class="contact__text">17 Tamsey Yard,<br>Upper Drisk, Kelbridge,<br>KX31 8RJ,<br>United Kingdom</span>
    </li>
  </ul>
</section>

</body>
</html>
```